Digital Health Records Service Landing page and site

I would like a reworking of the current Wordpress website to include the new logo. LedgerNest.online.
I want a more professional and corporate looking ( less homemade) landing page. I want a robust, reliable easy to maintain theme with minimal premium plugins.
I would like to use most of the current content minus the individual pricing box and minus the video or with a section/Page I can open/add to display a video if needed.
I would like it to be easy to customise, add pages or menu items without ruining the appearance. Clean, crisp, serious but not dull.
I want clear and visible social icons at the top. A clear call to action and form.

Project budget increased to attract better designers and get better results!

Target Market(s)

Charitable, Voluntary and Social Enterprise businesses in the UK and US

Industry/Entity Type

saas to business

Coding

Coded - Design and coding required

Font styles to use
Serif
Sans Serif

Colors

Designer to choose colors to be used in the design.

Requirements
Must have
• Clean, crisp, minimal, improved testimonial section and features section and FAQ
Should not have
• Purples, Browns, dark theme, corny stock images of therapists etc. Remember this is a digital records saas and not an online therapy site. Please no medical look, no doctors, no clinics etc.

```html
<!DOCTYPE html>
<html lang="en">
<head>
<meta charset="utf-8">
<title>LedgerNest.online</title>
<link href="https://fonts.googleapis.com/css2?family=Poppins:wght@400;500;600;700;800&display=swap" rel="stylesheet">
<style>
:root{
  --blue:#5b8fc9;
  --blue-soft:#c9daee;
  --ink:#333436;
  --muted:#666a70;
  --tint:#eef3fa;
  --card:#f2f6fb;
  --footer:#3c3c3e;
  --white:#ffffff;
}
*{margin:0;padding:0;box-sizing:border-box}
html,body{width:1200px;height:3974px;overflow:hidden}
body{position:relative;font-family:'Poppins',sans-serif;color:var(--ink);background:var(--white)}
.abs{position:absolute}
.bg-shape{position:absolute;left:0;top:0}
/* header */
.site-header{position:absolute;left:0;top:0;width:1200px;height:84px;background:var(--white);z-index:2}
.brand{position:absolute;left:88px;top:22px;display:flex;align-items:center;gap:10px;font-size:20px;font-weight:500;color:var(--ink)}
.brand-square{width:40px;height:40px;background:var(--blue)}
.main-nav{position:absolute;right:92px;top:30px;display:flex;gap:28px;font-size:15px;color:var(--ink);align-items:center}
.main-nav .active{color:var(--blue);font-weight:500}
.nav-social{display:flex;gap:10px;margin-left:-6px}
.nav-social span{width:10px;height:10px;border-radius:50%;background:var(--ink);display:block}
/* hero */
.hero-title{position:absolute;top:176px;width:1200px;text-align:center;color:var(--white);font-size:46px;font-weight:800;letter-spacing:0.5px}
.hero-sub{position:absolute;top:239px;width:1200px;text-align:center;color:var(--white);font-size:15px}
.btn{position:absolute;display:flex;align-items:center;justify-content:center;font-size:12px;font-weight:700;text-transform:uppercase;letter-spacing:0.3px}
.btn-solid-white{background:var(--white);color:var(--ink)}
.btn-outline-white{border:2px solid var(--white);color:var(--white)}
.btn-outline-dark{border:2px solid var(--ink);color:var(--ink);background:var(--white)}
.btn-blue{background:var(--blue);color:var(--white)}
.placeholder{position:absolute;border-radius:18px}
/* headings */
.section-title{position:absolute;width:1200px;text-align:center;font-size:36px;font-weight:700;color:var(--ink)}
.service-label{position:absolute;font-size:15px;font-weight:700;line-height:1.3;text-transform:uppercase}
.service-label.right-align{text-align:right}
.icon{position:absolute;fill:none;stroke:var(--ink);stroke-width:2.4;stroke-linecap:round;stroke-linejoin:round}
/* features */
.features-title{position:absolute;left:125px;top:1390px;font-size:40px;font-weight:700}
.features-text{position:absolute;left:125px;top:1446px;width:380px;font-size:15px;line-height:22.4px;color:var(--muted)}
/* practitioner */
.prac-card{position:absolute;top:1901px;width:234px;height:235px;background:var(--card);box-shadow:0 10px 28px rgba(60,90,130,0.12);text-align:center}
.prac-card svg{position:absolute;left:67px;top:36px;fill:none;stroke:var(--blue);stroke-width:2.4;stroke-linecap:round;stroke-linejoin:round}
.prac-card p{position:absolute;left:0;top:148px;width:234px;font-size:16px;font-weight:700;line-height:22px;text-transform:uppercase}
/* reviews */
.review-photo{position:absolute;left:186px;top:2299px;width:346px;height:346px;border-radius:50%}
.quote-mark{position:absolute;left:672px;top:2222px;font-size:260px;font-weight:800;color:#ececec;line-height:1}
.review-title{position:absolute;left:586px;top:2350px;font-size:39px;font-weight:700}
.review-text{position:absolute;left:586px;top:2405px;width:430px;font-size:15px;line-height:24px;color:var(--muted)}
.stars{position:absolute;left:586px;top:2486px;color:#f2a51a;font-size:16px;letter-spacing:1px}
.review-name{position:absolute;left:586px;top:2512px;font-size:16px;font-weight:700}
.review-role{position:absolute;left:586px;top:2540px;font-size:13px;font-weight:600;color:var(--muted)}
.review-dots{position:absolute;left:586px;top:2570px;display:flex;gap:12px}
.review-dots span{width:24px;height:2px;background:#c8c8c8}
.review-dots .on{background:var(--blue)}
/* faq */
.faq{position:absolute;left:214px;width:772px;background:var(--white);box-shadow:0 6px 22px rgba(0,0,0,0.08);border-radius:4px}
.faq h3{position:absolute;left:26px;font-size:18px;font-weight:500}
.faq .toggle{position:absolute;right:22px;font-size:18px;font-weight:500}
.faq.open{border-left:3px solid var(--blue)}
.faq.open p{position:absolute;left:26px;top:60px;width:720px;font-size:14.5px;line-height:22px;color:var(--muted)}
/* footer */
.reach-title{position:absolute;top:3474px;width:1200px;text-align:center;font-size:44px;font-weight:800;color:var(--white)}
.reach-sub{position:absolute;top:3530px;width:1200px;text-align:center;font-size:16px;color:var(--white)}
.footer-brand{position:absolute;left:167px;top:3740px;font-size:26px;font-weight:500;color:var(--white);line-height:1.1}
.footer-square{position:absolute;left:235px;top:3670px;width:58px;height:58px;background:var(--blue)}
.footer-social{position:absolute;left:181px;top:3830px;display:flex;gap:15px}
.footer-social span{width:37px;height:37px;border-radius:50%;border:2px solid #7b7b7e;display:block;position:relative}
.footer-social span::after{content:"";position:absolute;left:12px;top:12px;width:9px;height:9px;border-radius:2px;background:var(--white)}
.footer-col{position:absolute;top:3656px;color:var(--white)}
.footer-col h4{font-size:16px;font-weight:700;text-transform:uppercase;margin-bottom:14px}
.footer-col li{list-style:none;font-size:13px;line-height:31.3px;color:#e2e2e2}
.footer-col li::before{content:"›";color:#9a9a9d;margin-right:8px}
.footer-rule{position:absolute;left:88px;top:3918px;width:1024px;height:1px;background:#5a5a5d}
.copyright{position:absolute;top:3936px;width:1200px;text-align:center;font-size:12.5px;color:var(--white)}
.privacy{position:absolute;left:1028px;top:3936px;font-size:12.5px;color:var(--white)}
.to-top{position:absolute;left:1124px;top:3889px;width:40px;height:40px;border-radius:50%;background:var(--white);display:flex;align-items:center;justify-content:center;color:var(--ink);font-size:16px}
</style>
</head>
<body>

<svg class="bg-shape" width="1200" height="3974" viewBox="0 0 1200 3974" aria-hidden="true">
  <path d="M0 84 H1200 V505 C980 600 720 700 460 810 C260 890 70 850 0 600 Z" fill="var(--blue-soft)"/>
  <path d="M0 84 H1200 V478 C960 580 700 680 440 790 C250 860 60 800 0 570 Z" fill="var(--blue)"/>
  <path d="M0 1740 H1200 V2150 C1020 2190 900 2230 760 2240 C520 2250 260 1960 0 1910 Z" fill="var(--tint)"/>
  <path d="M0 3655 C260 3470 700 3330 1200 3320 V3974 H0 Z" fill="var(--blue)"/>
  <path d="M0 3680 C300 3500 700 3380 1200 3420 V3974 H0 Z" fill="var(--footer)"/>
  <path d="M700 3400 C900 3320 1100 3330 1200 3346 V3440 C1100 3380 900 3370 700 3400 Z" fill="var(--footer)"/>
</svg>

<header class="site-header">
  <div class="brand"><span class="brand-square"></span>LedgerNest.online</div>
  <nav class="main-nav">
    <span class="active">Home</span><span>About</span><span>Features</span><span>Security</span><span>Contact</span>
    <span class="nav-social" aria-label="Social links"><span></span><span></span><span></span><span></span></span>
  </nav>
</header>

<section class="hero">
  <h1 class="hero-title">THERAPIST DESIGNED CLIENT</h1>
  <p class="hero-sub">Simple to use,Secure,Client Management and Record Keeping for Practitioners and Teams</p>
  <div class="btn btn-solid-white" style="left:433px;top:282px;width:102px;height:37px">Sing In</div>
  <div class="btn btn-outline-white" style="left:547px;top:282px;width:219px;height:37px">Have an account? Sign In</div>
  <div class="placeholder" role="img" aria-label="Dashboard preview on laptop and phone with analytics charts" style="left:143px;top:359px;width:797px;height:462px;background:linear-gradient(135deg,#f4f7fb,#dfe8f3)"></div>
</section>

<section class="services">
  <h2 class="section-title" style="top:895px">OUR SERVICES</h2>
  <div class="service-label right-align" style="left:190px;top:1022px;width:137px">Audit and KPI<br>Monitoring</div>
  <svg class="icon" style="left:342px;top:1010px" width="62" height="62" viewBox="0 0 62 62"><rect x="6" y="6" width="36" height="46" rx="3"/><polyline points="12,20 18,14 24,22 30,12 36,18"/><rect x="12" y="30" width="8" height="8"/><line x1="24" y1="34" x2="34" y2="34"/><circle cx="44" cy="42" r="9"/><line x1="50" y1="49" x2="57" y2="57"/></svg>
  <div class="service-label right-align" style="left:190px;top:1128px;width:137px">Service<br>Creation</div>
  <svg class="icon" style="left:342px;top:1118px" width="62" height="62" viewBox="0 0 62 62"><rect x="6" y="6" width="44" height="48" rx="3"/><line x1="14" y1="16" x2="30" y2="16"/><line x1="14" y1="24" x2="26" y2="24"/><circle cx="40" cy="40" r="9"/><circle cx="40" cy="40" r="3"/><line x1="14" y1="46" x2="26" y2="34"/></svg>
  <div role="img" aria-label="LedgerNest mark" class="abs" style="left:490px;top:1000px;width:222px;height:215px;background:var(--blue)"></div>
  <div class="abs" style="left:758px;top:982px;width:5px;height:233px;background:var(--blue)"></div>
  <svg class="icon" style="left:796px;top:1010px" width="62" height="62" viewBox="0 0 62 62"><rect x="6" y="8" width="46" height="46" rx="3"/><line x1="6" y1="18" x2="52" y2="18"/><line x1="14" y1="28" x2="44" y2="28"/><line x1="14" y1="36" x2="44" y2="36"/><line x1="14" y1="44" x2="34" y2="44"/></svg>
  <div class="service-label" style="left:872px;top:1022px;width:150px">All Standard<br>Features</div>
  <svg class="icon" style="left:788px;top:1118px" width="66" height="66" viewBox="0 0 66 66"><rect x="20" y="6" width="38" height="50" rx="3"/><line x1="28" y1="18" x2="50" y2="18"/><line x1="34" y1="28" x2="50" y2="28"/><line x1="36" y1="38" x2="50" y2="38"/><circle cx="18" cy="46" r="13"/><polyline points="18,38 18,46 24,50"/></svg>
  <div class="service-label" style="left:869px;top:1128px;width:150px">Waiting List<br>Management</div>
  <div class="btn btn-outline-dark" style="left:521px;top:1260px;width:158px;height:39px">View all services</div>
</section>

<section class="features">
  <h2 class="features-title">FEATURES</h2>
  <p class="features-text">LedgerNest.online has been developed by experts in the field of mental health care, psychotherapy and counselling. Particular attention has been paid to its ‘ease of use’, adaptability to different client groups and the security of client information. The system has a highly...</p>
  <div class="btn btn-blue" style="left:125px;top:1605px;width:125px;height:39px">Read more</div>
  <div class="placeholder" role="img" aria-label="Dashboard preview on a desktop monitor" style="left:532px;top:1311px;width:543px;height:479px;background:linear-gradient(135deg,#f6f8fb,#dce6f2)"></div>
</section>

<section class="practitioner">
  <h2 class="section-title" style="top:1832px">PRACTITIONER</h2>
  <div class="prac-card" style="left:94px">
    <svg width="100" height="100" viewBox="0 0 100 100"><rect x="40" y="10" width="44" height="32" rx="2"/><line x1="62" y1="42" x2="62" y2="50"/><line x1="10" y1="54" x2="90" y2="54"/><rect x="62" y="58" width="24" height="34"/><line x1="62" y1="70" x2="86" y2="70"/><line x1="62" y1="82" x2="86" y2="82"/><rect x="14" y="36" width="18" height="26" rx="3"/><line x1="23" y1="62" x2="23" y2="90"/><line x1="12" y1="90" x2="34" y2="90"/></svg>
    <p>Global<br>Workspace</p>
  </div>
  <div class="prac-card" style="left:353px">
    <svg width="100" height="100" viewBox="0 0 100 100"><path d="M10 22 H36 L42 30 H86 V74 H10 Z"/><rect x="22" y="44" width="36" height="28" rx="2"/><line x1="30" y1="54" x2="50" y2="54"/><rect x="58" y="58" width="30" height="30" rx="2"/><line x1="73" y1="64" x2="73" y2="82"/><line x1="64" y1="73" x2="82" y2="73"/></svg>
    <p>Drag &amp; Drop<br>Summaries</p>
  </div>
  <div class="prac-card" style="left:612px">
    <svg width="100" height="100" viewBox="0 0 100 100"><rect x="8" y="14" width="84" height="58" rx="3"/><line x1="50" y1="72" x2="50" y2="84"/><line x1="34" y1="88" x2="66" y2="88"/><path d="M50 6 L72 14 V36 C72 50 62 58 50 62 C38 58 28 50 28 36 V14 Z"/><polyline points="40,34 48,42 62,28"/></svg>
    <p>Safeguarding<br>Monitoring</p>
  </div>
  <div class="prac-card" style="left:871px">
    <svg width="100" height="100" viewBox="0 0 100 100"><rect x="10" y="14" width="72" height="70" rx="4"/><line x1="10" y1="28" x2="82" y2="28"/><line x1="24" y1="6" x2="24" y2="20"/><line x1="46" y1="6" x2="46" y2="20"/><line x1="68" y1="6" x2="68" y2="20"/><circle cx="44" cy="56" r="16"/><polyline points="44,46 44,56 52,60"/><path d="M74 62 C74 54 90 54 90 62 V78 H74 Z"/></svg>
    <p>Event &amp; Review<br>Reminders</p>
  </div>
  <div class="btn btn-outline-dark" style="left:521px;top:2162px;width:158px;height:39px">View all services</div>
</section>

<section class="reviews">
  <div class="review-photo" role="img" aria-label="Portrait photo of a client, clinical director" style="background:radial-gradient(circle at 45% 40%,#e7dccf,#8aa6c2 70%,#5f7d9c)"></div>
  <div class="quote-mark" aria-hidden="true">“</div>
  <h2 class="review-title">CUSTOMER REVIEWS</h2>
  <p class="review-text">We wanted to achieve a secure easy to access system to store meaningful clinical data that could be easily audited to improve the quality of services...</p>
  <div class="stars">★★★★★</div>
  <div class="review-name">MAREN HOLT</div>
  <div class="review-role">Clinical director</div>
  <div class="review-dots"><span></span><span class="on"></span><span></span></div>
</section>

<section class="faqs">
  <h2 class="section-title" style="top:2732px">FAQs</h2>
  <div class="faq open" style="top:2791px;height:181px">
    <h3 style="top:22px">Security</h3><span class="toggle" style="top:20px">–</span>
    <p>Ensuring the safety and security of client data is our top priority.<br>Our system employs account permissions to ensure that client data can only be viewed by the relevant team members even when therapists work across different services or teams.<br>A strict password policy, two-factor authentication and account lockouts protect end-user accounts.</p>
  </div>
  <div class="faq" style="top:2985px;height:56px"><h3 style="top:15px">Secure Hosting and Secure Development</h3><span class="toggle" style="top:15px">+</span></div>
  <div class="faq" style="top:3056px;height:56px"><h3 style="top:15px">Compliant Daily Back-ups</h3><span class="toggle" style="top:15px">+</span></div>
  <div class="faq" style="top:3127px;height:56px"><h3 style="top:15px">Data Security Standards</h3><span class="toggle" style="top:15px">+</span></div>
  <div class="faq" style="top:3197px;height:56px"><h3 style="top:15px">Policies and Procedures</h3><span class="toggle" style="top:15px">+</span></div>
</section>

<footer class="site-footer">
  <h2 class="reach-title">REACH US</h2>
  <p class="reach-sub">Do not hesitate to ask us any questions</p>
  <div class="btn btn-blue" style="left:538px;top:3568px;width:122px;height:40px">Contact us</div>

  <div class="footer-square"></div>
  <div class="footer-brand">LedgerNest<br>.online</div>
  <div class="footer-social" aria-label="Social links"><span></span><span></span><span></span><span></span></div>

  <div class="footer-col" style="left:467px"><h4>Quick Links</h4><ul><li>Home</li><li>About</li><li>Features</li><li>Security</li><li>Contact</li></ul></div>
  <div class="footer-col" style="left:657px"><h4>Downloads</h4><ul><li>Insight Desktop</li><li>Insight Mobile</li><li>Insight Report Server</li><li>See all downloads</li></ul></div>
  <div class="footer-col" style="left:866px"><h4>Data Platform</h4><ul><li>Overview</li><li>Insight</li><li>Flow Apps</li><li>Flow Automate</li><li>Flow Virtual Agents</li></ul></div>

  <div class="footer-rule"></div>
  <div class="copyright">© 2023 LedgerNest.online All Rights Reserved.</div>
  <div class="privacy">Privacy Policy</div>
  <div class="to-top">↑</div>
</footer>

</body>
</html>
```